TKA Electricial Contracting Services

Hi guys, after a design for my small electrical company, have logo design files to be incorporated into the layout, the basic concept is electrical contracting services for residential, commercial, industrial & data services, image is clean clear and strong,

Card format is to have a nice clean logo on front,with maybe the Residential – commercial – industrial - data, followed with licensed & insured, followed by contact details on backside of the card.

Target Market(s)

Residential, commercial, industrial sectors.

Industry/Entity Type

Electrical

Contact Information for Business Card

TKA logo,
Residential – commercial – industrial - data
REC: 61372
Email: tka@poralink.net.au
Phone: 0458 203 719

Requirements
Must have
• Clean & strong design.
Nice to have
• If possible, I would like the logo colours inverted so the text is orange and the background is black on the front of the card, then the backside of the card be the reverse colour
Should not have
• No Sparks, lightning bolts,

```html
<!DOCTYPE html>
<html lang="en">
<head>
<meta charset="utf-8">
<title>TKA Electricial Contracting Services — Business Card</title>
<link rel="stylesheet" href="https://fonts.googleapis.com/css2?family=Exo+2:wght@300;600;700;800&display=swap">
<style>
  :root {
    --page: #e9e6e1;
    --orange-light: #ffc54a;
    --orange: #f7a21b;
    --orange-deep: #e4820c;
    --ink: #141414;
    --black: #0b0b0b;
    --charcoal: #262626;
    --white: #ffffff;
    --paper-white: #f1f1f1;
  }
  * { box-sizing: border-box; margin: 0; padding: 0; }
  html, body {
    width: 1200px; height: 900px; overflow: hidden;
    background: var(--page);
    font-family: "Exo 2", Arial, sans-serif;
  }
  .canvas { position: relative; width: 1200px; height: 900px; }

  .card {
    position: absolute;
    width: 560px; height: 320px;
    border-radius: 4px;
    overflow: hidden;
    box-shadow: 0 10px 30px rgba(0,0,0,.22);
  }

  /* ---------- Orange side ---------- */
  .card--contact {
    left: 50px; top: 120px;
    background: linear-gradient(135deg, var(--orange-deep) 0%, var(--orange) 45%, var(--orange-light) 100%);
  }
  .card--contact .brand {
    position: absolute; left: 36px; top: 48px;
    color: var(--ink);
  }
  .brand__name {
    font-weight: 800; font-size: 74px; line-height: .9; letter-spacing: -1px;
  }
  .brand__tag {
    font-weight: 700; font-size: 17px; margin-top: 6px; letter-spacing: .2px;
  }
  .contact {
    position: absolute; right: 26px; top: 26px;
    text-align: right; color: var(--ink);
    font-weight: 600;
  }
  .contact__line { display: flex; align-items: center; justify-content: flex-end; gap: 8px; }
  .contact__phone { font-size: 22px; }
  .contact__email { font-size: 16px; margin-top: 8px; }
  .contact svg { width: 14px; height: 14px; }

  .services {
    position: absolute; left: 0; right: 0; top: 174px; height: 66px;
    background: linear-gradient(180deg, var(--charcoal), var(--black));
    border-top: 3px solid var(--ink);
    color: var(--white);
    font-weight: 700; font-size: 14.5px; line-height: 1.35;
    padding: 13px 80px 0 26px;
  }
  .services__seal {
    position: absolute; right: 22px; top: 9px;
    width: 48px; height: 48px; border-radius: 50%;
    background: var(--orange); border: 3px solid var(--paper-white);
  }
  .registration {
    position: absolute; left: 0; right: 0; top: 240px; height: 34px;
    background: linear-gradient(180deg, var(--white), #d9d9d9);
    color: var(--ink);
    font-weight: 700; font-size: 16px;
    display: flex; align-items: center; justify-content: center;
  }
  .footer-band {
    position: absolute; left: 0; right: 0; top: 274px; bottom: 0;
    background: linear-gradient(90deg, var(--orange-deep), var(--orange));
  }

  /* ---------- Black side ---------- */
  .card--brand {
    left: 590px; top: 460px;
    background: var(--black);
  }
  .card--brand .texture {
    position: absolute; inset: 0;
    background: linear-gradient(160deg, #1c1c1c 0%, var(--black) 60%, #151515 100%);
  }
  .card--brand .brand {
    position: absolute; left: 150px; top: 70px;
    color: var(--orange);
  }
  .card--brand .brand__name { font-size: 96px; }
  .card--brand .brand__tag { font-size: 20px; }
  .sectors {
    position: absolute; left: 34px; bottom: 34px;
    display: flex; align-items: center; gap: 12px;
    color: var(--orange);
    font-weight: 300; font-size: 17px; letter-spacing: 3px;
  }
  .sectors__rule { width: 40px; height: 1px; background: var(--orange); }
</style>
</head>
<body>
<main class="canvas">

  <section class="card card--contact" aria-label="Business card, contact side">
    <div class="brand">
      <div class="brand__name">TKA</div>
      <div class="brand__tag">Tom Kessler Electrical</div>
    </div>

    <div class="contact">
      <div class="contact__line contact__phone">
        <span>0458 203 719</span>
        <svg viewBox="0 0 24 24" aria-hidden="true"><path fill="#141414" d="M6.6 10.8a15 15 0 0 0 6.6 6.6l2.2-2.2a1 1 0 0 1 1-.25 11.4 11.4 0 0 0 3.6.57 1 1 0 0 1 1 1V20a1 1 0 0 1-1 1A17 17 0 0 1 3 4a1 1 0 0 1 1-1h3.5a1 1 0 0 1 1 1c0 1.25.2 2.45.57 3.57a1 1 0 0 1-.25 1z"/></svg>
      </div>
      <div class="contact__line contact__email">
        <span>tka@poralink.net.au</span>
        <svg viewBox="0 0 24 24" aria-hidden="true"><rect x="2" y="5" width="20" height="14" fill="#141414"/><path d="M2 5l10 8 10-8" fill="none" stroke="#f7a21b" stroke-width="1.6"/></svg>
      </div>
    </div>

    <div class="services">
      <p>New installations Additions Rewiring Repairs Maintenance</p>
      <p>24 hours Faults and Emergency Assistance.</p>
      <span class="services__seal" aria-hidden="true"></span>
    </div>
    <div class="registration">REC: 61372</div>
    <div class="footer-band"></div>
  </section>

  <section class="card card--brand" aria-label="Business card, logo side">
    <div class="texture" role="img" aria-label="Faint repeating brand-name pattern on black"></div>
    <div class="brand">
      <div class="brand__name">TKA</div>
      <div class="brand__tag">Tom Kessler Electrical</div>
    </div>
    <div class="sectors">
      <span>COMMERCIAL - INDUSTRIAL - DATA</span>
      <span class="sectors__rule"></span>
    </div>
  </section>

</main>
</body>
</html>
```